Construction Company Facebook Banner

We are a small residential building company, building mostly new homes, renovations, extensions. our social media needs an uplift to look more professional.
I have no photos I wish to use in the banner as of yet however I have included the company logo, and the business card design which has some details.
I would like something simple but professional.
The banner does not need to have email, phone number, services provided etc. all of this is available on the facebook page itself. Something simple and clean please.
Industry/Entity Type
Construction
Requirements
Should not have
- Images of people, QR Code

```html
<!DOCTYPE html>
<html lang="en">
<head>
<meta charset="utf-8">
<title>Ridgeline Homes – Facebook Banner</title>
<link rel="stylesheet" href="https://fonts.googleapis.com/css2?family=Roboto:wght@500;700&family=Roboto+Condensed:wght@500&display=swap">
<style>
  :root {
    --backdrop: #d4d4d4;
    --panel-dark: #3b3b3b;
    --panel-light: #efefef;
    --text-light: #f2f2f2;
    --text-dark: #161616;
    --text-services: #2f2f2f;
    --brand-green: #0fa142;
  }
  * { margin: 0; padding: 0; box-sizing: border-box; }
  html, body {
    width: 1200px;
    height: 800px;
    overflow: hidden;
    background: var(--backdrop);
  }
  .banner {
    position: absolute;
    left: 0;
    top: 135px;
    width: 1200px;
    height: 530px;
    display: flex;
  }
  .banner__intro {
    position: relative;
    width: 597px;
    height: 100%;
    background: var(--panel-dark);
    color: var(--text-light);
    font-family: "Roboto", sans-serif;
  }
  .tagline {
    position: absolute;
    left: 78px;
    top: 40px;
    font-weight: 700;
    font-size: 80px;
    line-height: 96px;
    letter-spacing: 1px;
  }
  .contact {
    position: absolute;
    left: 80px;
    display: flex;
    align-items: center;
    font-weight: 500;
  }
  .contact svg { flex: none; }
  .contact__text { position: absolute; left: 78px; white-space: nowrap; }
  .contact--phone { top: 365px; height: 44px; font-size: 40px; }
  .contact--email { top: 438px; height: 40px; font-size: 30px; }

  .banner__brand {
    position: relative;
    width: 603px;
    height: 100%;
    background: var(--panel-light);
    text-align: center;
    font-family: "Roboto", sans-serif;
  }
  .brand-mark {
    position: absolute;
    left: 50%;
    top: 78px;
    width: 120px;
    height: 120px;
    margin-left: -60px;
    background: var(--brand-green);
  }
  .brand-name {
    position: absolute;
    left: 0;
    right: 0;
    top: 248px;
    color: var(--text-dark);
    font-weight: 700;
    text-transform: uppercase;
  }
  .brand-name__main { display: block; font-size: 50px; line-height: 58px; }
  .brand-name__sub { display: block; font-size: 25px; line-height: 34px; letter-spacing: 0.5px; }
  .services {
    position: absolute;
    left: 0;
    right: 0;
    top: 374px;
    color: var(--text-services);
    font-family: "Roboto Condensed", sans-serif;
    font-weight: 500;
    font-size: 38px;
    line-height: 46px;
  }
</style>
</head>
<body>
  <section class="banner">
    <div class="banner__intro">
      <h1 class="tagline">BUILDING<br>YOUR<br>FUTURE</h1>
      <div class="contact contact--phone">
        <svg width="44" height="44" viewBox="0 0 24 24" aria-hidden="true">
          <path fill="currentColor" d="M6.6 10.8c1.4 2.8 3.8 5.1 6.6 6.6l2.2-2.2c.3-.3.7-.4 1-.2 1.1.4 2.3.6 3.6.6.6 0 1 .4 1 1V20c0 .6-.4 1-1 1C10.6 21 3 13.4 3 4c0-.6.4-1 1-1h3.5c.6 0 1 .4 1 1 0 1.3.2 2.5.6 3.6.1.3 0 .7-.2 1L6.6 10.8z"/>
        </svg>
        <span class="contact__text">0400 123 456</span>
      </div>
      <div class="contact contact--email">
        <svg width="46" height="34" viewBox="0 0 46 34" aria-hidden="true">
          <rect x="2" y="2" width="42" height="30" fill="none" stroke="currentColor" stroke-width="3"/>
          <polyline points="2,2 23,20 44,2" fill="none" stroke="currentColor" stroke-width="3"/>
        </svg>
        <span class="contact__text">hello@ridgelinehomes.com.au</span>
      </div>
    </div>
    <div class="banner__brand">
      <div class="brand-mark" aria-hidden="true"></div>
      <p class="brand-name">
        <span class="brand-name__main">Ridgeline Homes</span>
        <span class="brand-name__sub">and Constructions Pty Ltd</span>
      </p>
      <p class="services">NEW HOMES •<br>RENOVATIONS • EXTENSIONS</p>
    </div>
  </section>
</body>
</html>
```